Business Card Design for Transmission Repair / Automotive Shop

Hello! We have a local transmission repair shop -- view our logo and shop colors here: http://www.brookvalegears.com

We are the largest volume transmission rebuilder in the area and we need a business card to reflect that. The card needs to have a front and back. The front should display the logo and contact details.

Contact details may include business address, phone number and website url, as well as email: derek@brookvalegears.com

The back could display a Google map with directions to the shop as well as "Free Towing Available"

If needed, address can be featured on the back and not on the front, as we do not want the front to be too wordy. You can also play around with the front only containing the logo with the slogan and the back with all the contact details. Social media icons should also be visible somewhere ( Facebook, Twitter, G+)

Target Market(s)

Car owners who need their transmission repaired or car repaired

Industry/Entity Type

Shop

Font styles to use
Sans Serif

Requirements
Must have
• Must be double sided
• Must have logo in the middle of the front side
• Must have similar grey colors as website is toned

```html
<!DOCTYPE html>
<html lang="en">
<head>
<meta charset="utf-8">
<title>Brookvale Transmission – Business Card</title>
<link rel="stylesheet" href="https://fonts.googleapis.com/css2?family=Tinos:wght@400;700&display=swap">
<style>
  :root {
    --backdrop: #e4e2de;
    --card: #55575a;
    --card-edge: #4a4c4f;
    --gold: #e0b21c;
    --ink-light: #d9d9d6;
    --accent-red: #b3262b;
    --map-land: #efe9d6;
    --icon-blue: #3f8fd2;
    --icon-red: #c8402f;
  }
  * { margin: 0; padding: 0; box-sizing: border-box; }
  html, body { width: 1200px; height: 800px; overflow: hidden; }
  body {
    background: var(--backdrop);
    font-family: "Tinos", "Times New Roman", serif;
    display: flex;
    align-items: center;
    justify-content: center;
    gap: 60px;
  }
  .card {
    position: relative;
    width: 525px;
    height: 300px;
    background: var(--card);
    border: 1px solid var(--card-edge);
    box-shadow: 0 10px 24px rgba(0,0,0,.18);
  }

  /* Front */
  .card--front .brand {
    position: absolute;
    left: 50%;
    top: 92px;
    transform: translateX(-50%);
    display: flex;
    align-items: center;
    gap: 10px;
    color: var(--ink-light);
    font-size: 24px;
    font-weight: 700;
    white-space: nowrap;
  }
  .brand-dot {
    width: 20px;
    height: 20px;
    border-radius: 50%;
    background: var(--accent-red);
    flex: none;
  }
  .card--front .slogan {
    position: absolute;
    left: 40px;
    top: 168px;
    width: 445px;
    color: var(--gold);
    font-size: 18px;
    line-height: 1.35;
  }

  /* Back */
  .card--back .contact {
    position: absolute;
    left: 28px;
    top: 24px;
    width: 230px;
    color: var(--ink-light);
    font-size: 12.5px;
    line-height: 1.45;
  }
  .contact .company {
    display: flex;
    align-items: center;
    gap: 6px;
    color: var(--gold);
    font-weight: 700;
    font-size: 15px;
    margin-bottom: 2px;
  }
  .company-dot {
    width: 9px;
    height: 9px;
    border-radius: 50%;
    background: var(--accent-red);
    flex: none;
  }
  .card--back .towing {
    position: absolute;
    left: 28px;
    bottom: 24px;
    display: flex;
    align-items: center;
    gap: 6px;
    color: var(--ink-light);
    font-size: 12.5px;
  }
  .map {
    position: absolute;
    right: 28px;
    top: 24px;
    width: 220px;
    height: 170px;
    background: linear-gradient(135deg, var(--map-land) 0%, #e4e0d4 60%, #dcd8cc 100%);
    border: 2px solid #f4f1e8;
  }
  .social {
    position: absolute;
    right: 28px;
    top: 210px;
    display: flex;
    gap: 6px;
  }
  .social-box {
    width: 22px;
    height: 22px;
    border-radius: 3px;
  }
  .social-box--one { background: var(--icon-blue); opacity: .75; }
  .social-box--two { background: var(--icon-blue); }
  .social-box--three { background: var(--icon-red); }
</style>
</head>
<body>

  <section class="card card--front" aria-label="Card front">
    <div class="brand">
      <span class="brand-dot"></span>
      <span class="brand-name">Brookvale</span>
    </div>
    <p class="slogan">Largest Volume Transmission Rebuilder<br>in the Carolinas</p>
  </section>

  <section class="card card--back" aria-label="Card back">
    <div class="contact">
      <p class="company"><span class="company-dot"></span>Brookvale Transmission</p>
      <p>48 Foundry Lane, Ste B</p>
      <p>Millbrook, NC 28110</p>
      <p>704-555-0182</p>
      <p>www.brookvalegears.com</p>
      <p>derek@brookvalegears.com</p>
    </div>
    <p class="towing"><span class="company-dot"></span>Free Towing Available</p>
    <div class="map" role="img" aria-label="Street map showing directions to the shop"></div>
    <div class="social" aria-label="Social media">
      <span class="social-box social-box--one"></span>
      <span class="social-box social-box--two"></span>
      <span class="social-box social-box--three"></span>
    </div>
  </section>

</body>
</html>
```